8x8 Social Media Ad - Harbor Summit Expo

Attention Real Estate Agents
Please join us for our
Quarterly Real Estate Training Expo
The 2nd Saturday of February, May, August and November
Our Next Training Expo is _________________________________
From 9 am to 1 pm
at
Marlowe Suites Fernridge Station
4187 Copperleaf Lane, Greenbelt, MD 20770
Scheduled Speakers
9:00 am - Desmond Pryce - Orientation
9:30 am - Terrell Oakes - Multiple Income Streams / Keystone Track
10:00 am - Lorna Beckett - Marketing though Social Media
10:45 am - Raul Denning - Generating Business through Kelp-Nest
11:30 am - Tunde Adesemi - Real Estate Investing
12:15 pm - Marcus Oyelowo - (Main Speaker) Training Topic TBA
For more information call Desmond Pryce at (240) 555-0192 or email dpryce@harborsummithomes.example

```html
<!DOCTYPE html>
<html lang="en">
<head>
<meta charset="utf-8">
<title>Harbor Summit Expo – Quarterly Real Estate Training Expo</title>
<link rel="stylesheet" href="https://fonts.googleapis.com/css2?family=Bebas+Neue&family=Oswald:wght@500&family=Poppins:wght@400;500;600;700;800;900&display=swap">
<style>
  :root{
    --teal:#0b9294;
    --teal-light:#4fb8b8;
    --ink:#151515;
    --dark:#151515;
    --white:#ffffff;
    --ring:#5d5d5f;
    --photo-a:#8a8d92;
    --photo-b:#4a4c51;
  }
  *{margin:0;padding:0;box-sizing:border-box}
  html,body{width:1200px;height:1200px;overflow:hidden;background:#fff}
  .ad{position:relative;width:1200px;height:1200px;overflow:hidden;font-family:'Poppins',sans-serif;color:var(--ink);background:var(--white)}
  .abs{position:absolute}

  /* header */
  .brand{left:58px;top:92px;width:340px;display:flex;align-items:center;gap:14px}
  .brand-mark{width:22px;height:22px;background:var(--teal);flex:none}
  .brand-name{font-family:'Poppins',sans-serif;font-weight:700;font-size:30px;line-height:1.15;color:var(--teal);text-transform:uppercase}
  .attention{left:447px;top:48px;font-weight:900;font-size:56px;line-height:1;color:var(--teal);letter-spacing:-1px;white-space:nowrap}
  .agents{left:446px;top:112px;font-weight:900;font-size:60px;line-height:1;letter-spacing:0;white-space:nowrap}
  .join{left:447px;top:178px;font-weight:500;font-size:50px;line-height:1;letter-spacing:0.5px;white-space:nowrap}

  /* title band */
  .band{left:0;top:255px;width:1200px;height:137px;background:var(--teal)}
  .title{left:0;top:279px;width:1200px;text-align:center;font-family:'Bebas Neue',sans-serif;font-weight:400;font-size:88px;line-height:1;color:var(--white);-webkit-text-stroke:2px var(--ink);letter-spacing:0;white-space:nowrap}

  /* backdrop */
  .skyline{left:0;top:392px;width:1200px;height:389px;background:linear-gradient(180deg,#fbfbfb 0%,#eceded 55%,#d9dadb 100%)}
  .dark{left:0;top:781px;width:1200px;height:419px;background:var(--dark)}

  .dates{left:0;top:398px;width:1200px;text-align:center;font-weight:700;font-size:49px;line-height:52px;letter-spacing:-0.5px}

  .next{left:82px;top:512px;width:1036px;height:54px;border:2px solid var(--teal);border-radius:14px;background:var(--white);overflow:hidden}
  .next-label{position:absolute;left:0;top:0;width:466px;height:100%;background:var(--teal);border-radius:0 14px 14px 0;color:var(--white);font-weight:600;font-size:31px;line-height:50px;padding-left:22px;white-space:nowrap}

  .hours{left:91px;top:578px;font-family:'Bebas Neue',sans-serif;font-size:70px;line-height:70px;color:var(--ink);white-space:nowrap}
  .divider{left:512px;top:590px;width:2px;height:46px;background:var(--ink)}
  .pin{left:534px;top:588px;width:22px;height:28px}
  .venue{left:566px;top:584px;font-weight:700;font-size:23px;line-height:28px;letter-spacing:0.2px;white-space:nowrap}
  .address{left:566px;top:614px;font-weight:400;font-size:19px;line-height:26px;white-space:nowrap}

  /* speakers */
  .bracket{left:136px;top:677px;width:921px;height:60px;border:2px solid var(--ink);border-bottom:none;border-radius:18px 18px 0 0}
  .speakers-label{left:405px;top:677px;width:376px;height:33px;background:var(--ink);border-radius:0 0 12px 12px;color:var(--white);font-weight:600;font-size:21px;line-height:33px;text-align:center;letter-spacing:5px}

  .main-panel{left:968px;top:702px;width:178px;height:430px;background:var(--teal);border-radius:89px 89px 6px 6px}

  .portrait{width:160px;height:160px;border-radius:50%;background:var(--ring);display:flex;align-items:center;justify-content:center}
  .portrait .photo{width:136px;height:136px;border-radius:50%;background:radial-gradient(circle at 50% 35%,var(--photo-a),var(--photo-b))}
  .portrait.featured{width:168px;height:168px;background:var(--teal-light)}

  .sep{top:813px;width:0;height:255px;border-left:1px dashed #9a9a9a}

  .speaker{top:876px;width:180px;text-align:center;color:var(--white)}
  .speaker .time{font-weight:700;font-size:18px;line-height:24px}
  .speaker .name{font-weight:700;font-size:21px;line-height:24px;color:var(--teal);margin-top:4px;text-transform:uppercase;min-height:48px}
  .speaker .rule{width:36px;height:2px;background:var(--white);margin:13px auto 13px}
  .speaker .topic{font-size:16px;line-height:20px}
  .speaker.main .name{color:var(--ink)}
  .speaker.main .role{font-size:16px;line-height:18px}
  .speaker.main .topic{font-size:22px;line-height:28px}

  /* contact */
  .contact{left:68px;top:1090px;width:873px;height:41px;border:2px solid var(--teal);border-radius:22px}
  .contact-label{left:84px;top:1090px;font-family:'Oswald',sans-serif;font-weight:500;font-size:17.5px;line-height:41px;color:var(--white);letter-spacing:0.4px;white-space:nowrap}
  .contact-label span{color:var(--teal)}
  .contact-pill{left:481px;top:1090px;width:460px;height:41px;background:var(--teal);border-radius:22px;display:flex;align-items:center;gap:5px;padding-left:16px;color:var(--white);font-weight:600;font-size:13.5px;white-space:nowrap}
  .contact-pill svg{flex:none}
  .contact-pill .gap{width:6px}
</style>
</head>
<body>
<main class="ad">

  <div class="abs brand">
    <div class="brand-mark"></div>
    <div class="brand-name">Harbor Summit<br>Realty Group</div>
  </div>
  <div class="abs attention">ATTENTION</div>
  <div class="abs agents">REAL ESTATE AGENTS!</div>
  <div class="abs join">PLEASE JOIN US FOR OUR</div>

  <div class="abs band"></div>
  <h1 class="abs title">QUARTERLY REAL ESTATE TRAINING EXPO</h1>

  <div class="abs skyline" role="img" aria-label="Faded city skyline photograph"></div>
  <div class="abs dark"></div>

  <p class="abs dates">THE 2ND SATURDAY OF<br>FEBRUARY, MAY, AUGUST AND NOVEMBER</p>

  <div class="abs next"><div class="next-label">Our Next Training Expo is</div></div>

  <div class="abs hours">FROM 9 AM TO 1 PM</div>
  <div class="abs divider"></div>
  <svg class="abs pin" viewBox="0 0 22 28" aria-hidden="true"><path d="M11 1C5.5 1 1.5 5 1.5 10.3 1.5 17 11 27 11 27s9.5-10 9.5-16.7C20.5 5 16.5 1 11 1z" fill="#0b9294"/><circle cx="11" cy="10.3" r="3.6" fill="#fff"/></svg>
  <div class="abs venue">MARLOWE SUITES FERNRIDGE STATION</div>
  <div class="abs address">4187 Copperleaf Lane, Greenbelt, MD 20770</div>

  <div class="abs bracket"></div>
  <div class="abs speakers-label">SCHEDULED SPEAKERS</div>

  <div class="abs main-panel"></div>

  <div class="abs portrait" style="left:60px;top:712px"><div class="photo" role="img" aria-label="Portrait of Desmond Pryce"></div></div>
  <div class="abs portrait" style="left:242px;top:712px"><div class="photo" role="img" aria-label="Portrait of Terrell Oakes"></div></div>
  <div class="abs portrait" style="left:428px;top:712px"><div class="photo" role="img" aria-label="Portrait of Lorna Beckett"></div></div>
  <div class="abs portrait" style="left:611px;top:712px"><div class="photo" role="img" aria-label="Portrait of Raul Denning"></div></div>
  <div class="abs portrait" style="left:801px;top:712px"><div class="photo" role="img" aria-label="Portrait of Tunde Adesemi"></div></div>
  <div class="abs portrait featured" style="left:973px;top:708px"><div class="photo" role="img" aria-label="Portrait of Marcus Oyelowo"></div></div>

  <div class="abs sep" style="left:231px"></div>
  <div class="abs sep" style="left:415px"></div>
  <div class="abs sep" style="left:600px"></div>
  <div class="abs sep" style="left:786px"></div>

  <div class="abs speaker" style="left:50px">
    <div class="time">9:00 AM</div><div class="name">Desmond<br>Pryce</div><div class="rule"></div>
    <div class="topic">Orientation</div>
  </div>
  <div class="abs speaker" style="left:232px">
    <div class="time">9:30 AM</div><div class="name">Terrell<br>Oakes</div><div class="rule"></div>
    <div class="topic">Multiple<br>Income<br>Streams / Keystone<br>Track</div>
  </div>
  <div class="abs speaker" style="left:418px">
    <div class="time">10.00 AM</div><div class="name">Lorna<br>Beckett</div><div class="rule"></div>
    <div class="topic">Marketing<br>through Social<br>Media</div>
  </div>
  <div class="abs speaker" style="left:601px">
    <div class="time">10.45 AM</div><div class="name">Raul Denning</div><div class="rule"></div>
    <div class="topic">Generating<br>Business through<br>Kelp-Nest</div>
  </div>
  <div class="abs speaker" style="left:791px">
    <div class="time">11:30 AM</div><div class="name">Tunde<br>Adesemi</div><div class="rule"></div>
    <div class="topic">Real Estate<br>Investing</div>
  </div>
  <div class="abs speaker main" style="left:967px">
    <div class="time">12:15 PM</div><div class="name">Marcus<br>Oyelowo</div>
    <div class="role">(Main Speaker)</div><div class="rule"></div>
    <div class="topic">Training<br>Topic TBA</div>
  </div>

  <div class="abs contact"></div>
  <div class="abs contact-label">FOR MORE INFORMATION CALL <span>DESMOND PRYCE</span></div>
  <div class="abs contact-pill">
    <svg width="13" height="13" viewBox="0 0 24 24" aria-hidden="true"><path fill="#151515" d="M6.6 10.8a15.1 15.1 0 0 0 6.6 6.6l2.2-2.2c.3-.3.7-.4 1-.2 1.1.4 2.3.6 3.6.6.6 0 1 .4 1 1V20c0 .6-.4 1-1 1A17 17 0 0 1 3 4c0-.6.4-1 1-1h3.5c.6 0 1 .4 1 1 0 1.2.2 2.4.6 3.6.1.3 0 .7-.2 1z"/></svg>
    <span>(240) 555-0192</span><span class="gap"></span>
    <svg width="14" height="11" viewBox="0 0 24 18" aria-hidden="true"><rect x="1" y="1" width="22" height="16" fill="none" stroke="#151515" stroke-width="2"/><path d="M1 1l11 9 11-9" fill="none" stroke="#151515" stroke-width="2"/></svg>
    <span>dpryce@harborsummithomes.example</span>
  </div>

</main>
</body>
</html>
```